Summer Sunglass offer

Need a poster design for a spring / summer campaign. We are an opticians with good footfall. The design needs to be eye catching and aimed at 40 year old plus. The offer is Up to 50% off sunglass offer, t&c apply. (I have attached our last year campaign)
Also need a 2 sided A5 leaflet design (see attached)
I've uploaded a copy of our logo

A5 leaflet should read:

Grab a bargain on two great looks this summer Upto 50% off sunglasses
Look great and stay safe in the sun this summer

We want you to look great, feel fantastic and most of all stay safe in the sun this summer. That’s why we’re offering you 50% off prescription sunglasses with every complete pair of glasses you buy this summer or 25% off for prescription sunglasses with no other purchase.
Find you new summer looks from our gorgeous collection of frames in store. It matters to us that you look great in your new glasses as much as how well you see through them, so we’ll be on hand to help you find frames that suit you best.
What new looks will you go for? Smart or sassy? Formal or Fun? Whatever you’re in the mood for, you’ll find it in our collections this summer.
Call in today to find your new looks, and remember to bring your prescription if you don’t need an eye test.

Target Market(s)

40 + year old

Industry/Entity Type

Optician

Colors

Designer to choose colors to be used in the design.

Requirements
Must have
• Images, preferably a male and Female image

```html
<!DOCTYPE html>
<html lang="en">
<head>
<meta charset="utf-8">
<title>Summer Sunglass Offer – A5 Leaflet</title>
<link href="https://fonts.googleapis.com/css2?family=Ubuntu:wght@400;500&family=Open+Sans:wght@300;400;600;700&family=Oswald:wght@600&display=swap" rel="stylesheet">
<style>
  :root {
    --backdrop: #e9e1d6;
    --paper: #ffffff;
    --orange: #f1941f;
    --orange-deep: #ec8a16;
    --headline-red: #a3311d;
    --teal: #3b8f95;
    --navy: #1e3d7b;
    --sky: #2b73b7;
    --white: #ffffff;
  }
  * { box-sizing: border-box; margin: 0; padding: 0; }
  html, body { width: 1200px; height: 794px; overflow: hidden; }
  body { background: var(--backdrop); position: relative; font-family: "Open Sans", sans-serif; }

  .leaflet {
    position: absolute; top: 42px; width: 506px; height: 710px;
    overflow: hidden; background: var(--paper);
    box-shadow: 0 6px 18px rgba(0,0,0,.18);
  }
  .leaflet--front { left: 77px; }
  .leaflet--back { left: 616px; }

  .photo { position: absolute; left: 0; right: 0; }
  .leaflet--front .photo {
    top: 0; bottom: 0;
    background:
      radial-gradient(ellipse 60% 70% at 78% 45%, #c8875a 0%, #a86a44 35%, rgba(168,106,68,0) 70%),
      linear-gradient(180deg, #e7c070 0%, #6cc1cf 12%, #86cbd3 40%, #9fd3d4 62%, #d7e6e2 80%, #cfa788 100%);
  }
  .leaflet--back .photo {
    top: 0; height: 442px;
    background:
      radial-gradient(ellipse 38% 48% at 30% 58%, #b98566 0%, #7a5540 45%, rgba(40,60,100,0) 80%),
      linear-gradient(180deg, #2b6fb2 0%, #2f7cc0 45%, #5aa7cf 75%, #7bbdd0 100%);
  }

  .header-band {
    position: absolute; top: 24px; left: 0; width: 100%; height: 97px;
    background: linear-gradient(90deg, var(--paper) 0%, var(--paper) 62%, rgba(255,255,255,0) 88%);
    display: flex; align-items: center; padding-left: 46px; gap: 10px;
  }
  .brand-dot { width: 34px; height: 34px; border-radius: 50%; background: var(--teal); }
  .brand-name {
    font-family: "Ubuntu", sans-serif; font-weight: 500; color: var(--teal);
    font-size: 19px; line-height: 1.1; letter-spacing: 1.5px; text-transform: uppercase;
  }

  .offer-burst { position: absolute; left: 75px; top: 214px; width: 200px; height: 200px; }
  .offer-burst svg { position: absolute; inset: 0; }
  .offer-burst__text {
    position: absolute; inset: 0; display: flex; flex-direction: column;
    align-items: center; justify-content: center; color: var(--white); text-align: center;
  }
  .offer-burst__small { font-family: "Open Sans", sans-serif; font-weight: 700; font-size: 23px; line-height: 1; }
  .offer-burst__big { font-family: "Oswald", sans-serif; font-weight: 600; font-size: 74px; line-height: .95; letter-spacing: -2px; }

  .front-band {
    position: absolute; left: 0; top: 497px; width: 100%; height: 136px;
    background: linear-gradient(90deg, var(--orange-deep), var(--orange) 80%, rgba(241,148,31,.85));
    padding: 30px 0 0 43px;
  }
  .front-band__headline {
    font-family: "Ubuntu", sans-serif; font-weight: 500; color: var(--headline-red);
    font-size: 21px; line-height: 26px;
  }
  .front-band__sub {
    font-family: "Open Sans", sans-serif; color: var(--white);
    font-size: 16.5px; margin-top: 10px;
  }

  .back-headline {
    position: absolute; left: 250px; top: 158px; width: 240px;
    font-family: "Ubuntu", sans-serif; color: var(--white);
    font-size: 20.5px; line-height: 25.5px;
  }
  .back-sub {
    position: absolute; left: 250px; top: 281px; width: 240px;
    font-family: "Open Sans", sans-serif; color: var(--white);
    font-size: 15.5px; line-height: 20.5px;
  }

  .back-body {
    position: absolute; left: 0; top: 442px; width: 100%; height: 226px;
    background: linear-gradient(90deg, var(--orange-deep), var(--orange) 70%, #f3a64a);
    padding: 12px 38px 0 43px;
    font-family: "Open Sans", sans-serif; font-weight: 300; color: var(--white);
    font-size: 11.6px; line-height: 15.5px;
  }
  .back-body__question { font-weight: 600; }
  .back-body__call { font-weight: 600; color: var(--navy); }

  .back-footer {
    position: absolute; left: 0; bottom: 0; width: 100%; height: 42px;
    background: var(--paper); display: flex; align-items: center; justify-content: center;
    font-family: "Ubuntu", sans-serif; font-weight: 500; color: var(--navy); font-size: 11.5px;
  }
</style>
</head>
<body>

<section class="leaflet leaflet--front">
  <div class="photo" role="img" aria-label="Woman in dark sunglasses looking out over a tropical beach with palm trees and turquoise sea"></div>
  <header class="header-band">
    <span class="brand-dot"></span>
    <span class="brand-name">Bramley<br>Eyecare Centre</span>
  </header>
  <div class="offer-burst">
    <svg viewBox="-100 -100 200 200" aria-hidden="true">
      <polygon fill="#f1941f" points="100,0 84.4,16.8 92.4,38.3 71.5,47.8 70.7,70.7 47.8,71.5 38.3,92.4 16.8,84.4 0,100 -16.8,84.4 -38.3,92.4 -47.8,71.5 -70.7,70.7 -71.5,47.8 -92.4,38.3 -84.4,16.8 -100,0 -84.4,-16.8 -92.4,-38.3 -71.5,-47.8 -70.7,-70.7 -47.8,-71.5 -38.3,-92.4 -16.8,-84.4 0,-100 16.8,-84.4 38.3,-92.4 47.8,-71.5 70.7,-70.7 71.5,-47.8 92.4,-38.3 84.4,-16.8"/>
    </svg>
    <div class="offer-burst__text">
      <span class="offer-burst__small">UPTO</span>
      <span class="offer-burst__big">50%</span>
      <span class="offer-burst__small">OFFER</span>
    </div>
  </div>
  <div class="front-band">
    <h1 class="front-band__headline">Grab a bargain on two great looks<br>this summer Upto 50% off sunglasses</h1>
    <p class="front-band__sub">Look great and stay safe in the sun this summer</p>
  </div>
</section>

<section class="leaflet leaflet--back">
  <div class="photo" role="img" aria-label="Man wearing red-lensed sunglasses against a blue sky with palm trees and a tropical shoreline"></div>
  <header class="header-band">
    <span class="brand-dot"></span>
    <span class="brand-name">Bramley<br>Eyecare Centre</span>
  </header>
  <h2 class="back-headline">Grab a bargain on two great looks this summer Upto 50% off sunglasses</h2>
  <p class="back-sub">Look great and stay safe in the sun this summer</p>
  <div class="back-body">
    <p>We want you to look great, feel fantastic and most of all stay safe in the sun this summer. That’s why we’re offering you 50% off prescription sunglasses with every complete pair of glasses you buy this summer or 25% off for prescription sunglasses with no other purchase.</p>
    <p>Find you new summer looks from our gorgeous collection of frames in store. It matters to us that you love how you look in your new glasses as much as how well you see through them, so we’ll be on hand to help you find frames that suit you best.</p>
    <p><span class="back-body__question">What new looks will you go for? Smart or sassy? Formal or Fun?</span> Whatever you’re in the mood for, you’ll find it in our collections this summer.</p>
    <p class="back-body__call">Call in today to find your new looks, and remember to bring your prescription if you don’t need an eye test.</p>
  </div>
  <footer class="back-footer">42 Market St, Bramley, BR9 4QT. | 01632960418 | info@bramleyeyecare.co.uk</footer>
</section>

</body>
</html>
```